Plakat-Design für Musikwettbewerb-Veranstalter
Zielgruppe
Wir veranstalten Musikwettbewerbe an Schulen. Zielgruppe sind Schüler und ihre Eltern, männlich/weiblich 40/60, u25/ü25 ca. 50/50
Aufgabenstellung
Wir sind gespannt, gerne frei denken, Logo anbei, weitere Infos auf der Homepage www.klangfuchs-wettbewerb.de, Inhalte lt. altem Plakat (ebenfalls anbei)

```html
<!DOCTYPE html>
<html lang="de">
<head>
<meta charset="utf-8">
<title>Klangfuchs – Vorentscheid Holmbüll</title>
<link rel="stylesheet" href="https://fonts.googleapis.com/css2?family=Archivo+Black&family=Allerta+Stencil&family=Bitter:wght@400;700&display=swap">
<style>
  :root {
    --page: #ffffff;
    --paper: #ffffff;
    --sun: #fbe90b;
    --sky: #1ea3dc;
    --magenta: #e4247f;
    --ink: #1a1a1a;
    --purple: #6b3aa0;
    --orange: #f39a16;
    --lime: #8cc63f;
  }
  * { box-sizing: border-box; margin: 0; padding: 0; }
  html, body { width: 1174px; height: 1200px; overflow: hidden; background: var(--page); }
  .poster {
    position: absolute; left: 198px; top: 50px; width: 778px; height: 1100px;
    background: var(--paper); overflow: hidden;
    font-family: "Bitter", serif; color: var(--ink);
  }
  .artwork {
    position: absolute; left: 20px; top: 0; width: 738px; height: 345px;
    background: radial-gradient(ellipse at 20% 55%, rgba(228,36,127,.85), transparent 45%),
                radial-gradient(ellipse at 45% 30%, rgba(243,154,22,.85), transparent 40%),
                radial-gradient(ellipse at 55% 65%, rgba(107,58,160,.8), transparent 40%),
                radial-gradient(ellipse at 75% 45%, rgba(140,198,63,.85), transparent 40%),
                radial-gradient(ellipse at 92% 55%, rgba(251,233,11,.9), transparent 40%),
                radial-gradient(ellipse at 35% 85%, rgba(30,163,220,.75), transparent 35%);
  }
  .title {
    position: absolute; left: 0; width: 100%; top: 150px; text-align: center;
    font-family: "Archivo Black", sans-serif; font-size: 122px; line-height: 1;
    color: #fff; letter-spacing: -3px;
  }
  .stencil { font-family: "Allerta Stencil", sans-serif; text-transform: uppercase; line-height: 1; }
  .round { position: absolute; left: 42px; top: 352px; font-size: 86px; color: var(--sky); font-weight: 700; letter-spacing: -1px; }
  .town { position: absolute; left: 42px; top: 448px; font-size: 66px; color: var(--sky); letter-spacing: -1px; }
  .date { position: absolute; left: 372px; top: 434px; font-size: 68px; color: var(--magenta); letter-spacing: -1px; }
  .time { position: absolute; left: 420px; top: 510px; font-size: 34px; color: var(--magenta); }
  .crowd {
    position: absolute; left: 0; top: 520px; width: 100%; height: 300px;
    background: linear-gradient(to bottom, rgba(251,233,11,0) 0%, rgba(251,233,11,.55) 55%, var(--sun) 85%);
  }
  .band { position: absolute; left: 0; top: 800px; width: 100%; height: 300px; background: var(--sun); }
  .schools { position: absolute; left: 0; width: 100%; top: 576px; text-align: center; }
  .schools li { list-style: none; font-size: 41px; height: 72px; letter-spacing: 0.5px; }
  .venue, .admission {
    position: absolute; top: 790px; font-size: 20px; line-height: 27px; text-align: center;
  }
  .venue { left: 70px; width: 250px; }
  .admission { left: 490px; width: 200px; }
  .venue strong { font-weight: 700; }
  .apply { position: absolute; top: 928px; width: 100%; text-align: center; font-size: 19px; color: var(--sky); }
  .links { position: absolute; top: 982px; width: 100%; text-align: center; font-size: 19px; }
  .sponsors {
    position: absolute; top: 1034px; left: 36px; right: 36px;
    display: flex; justify-content: space-between; align-items: center;
    font-size: 19px; font-weight: 700;
  }
  .sponsor { display: flex; align-items: center; gap: 6px; }
  .sponsor .mark { width: 14px; height: 14px; background: var(--ink); }
  .sponsor .mark.round-mark { border-radius: 50%; }
</style>
</head>
<body>
  <main class="poster">
    <div class="artwork" role="img" aria-label="Bunte Silhouetten von Musikinstrumenten: Gitarren, Tuba, Schlagzeug, Keyboard, Mikrofon mit Farbspritzern"></div>
    <h1 class="title">Klangfuchs</h1>

    <div class="stencil round">Vorentscheid</div>
    <div class="stencil town">Holmbüll</div>
    <div class="stencil date">24.06.2017</div>
    <div class="stencil time">ab 19:00 Uhr</div>

    <div class="crowd" role="img" aria-label="Gelbe Silhouette eines jubelnden Publikums mit erhobenen Armen"></div>
    <div class="band"></div>

    <ul class="schools stencil">
      <li>Lindenhof-Schule</li>
      <li>Berufliche Schule Holmbüll</li>
      <li>Gemeinschaftsschule Holmbüll</li>
    </ul>

    <address class="venue" style="font-style:normal">
      <strong>Mensa der</strong><br>
      <strong>Lindenhof-Schule</strong><br>
      Lindenhofweg 5<br>
      24999 Holmbüll
    </address>
    <p class="admission">
      Einlass: 18:30 Uhr<br>
      Beginn: 19:00 Uhr<br>
      Vvk: 3 € | Ak: 4 €
    </p>

    <p class="apply">Bewerbung für Künstler unter www.klangfuchs-wettbewerb.de/bewerbung</p>
    <p class="links">www.klangfuchs-wettbewerb.de | social.klangfuchs-wettbewerb.de</p>

    <div class="sponsors">
      <span class="sponsor"><span class="mark"></span>Kreisbank</span>
      <span class="sponsor"><span class="mark round-mark"></span>Tonwerk</span>
      <span class="sponsor"><span class="mark"></span>Notenrecht</span>
      <span class="sponsor">Saitenhaus</span>
      <span class="sponsor"><span class="mark"></span>Ministerium Nord</span>
    </div>
  </main>
</body>
</html>
```